Einladungskarte
Zielgruppe
Hochzeitsgäste zwischen 30 und 40
Aufgabenstellung
Die Einladung hat folgende Eckdaten:
- Format Din A5 (Doppelseitiger DinA 4 gefalzt) Einladungsbogen (wird leichter Karton)
- Zusätzlicher Einlagebogen für Einladungstext
- Stil klassisch/elegant eher schlicht aber jung
- Grundthema Gerberablume (weiß, beige, rot oder orange)
- Hintergrund (hell)
- Zusätzlich zur Einladung wird Bildrecht der Blume für ein Banner auf der Hochzeitswebseite benötigt
- Editierbare Graphikdatei wird benötigt (da der Text der Einladung noch nicht final ist)

```html
<!DOCTYPE html>
<html lang="de">
<head>
<meta charset="utf-8">
<title>Einladung zur Hochzeit – Lena & Jonas</title>
<link rel="stylesheet" href="https://fonts.googleapis.com/css2?family=Marcellus&display=swap">
<style>
  :root {
    --cream: #f2e2c9;
    --paper: #ffffff;
    --gerbera-red: #c3111f;
    --gerbera-deep: #a80e1b;
    --stem-line: #e9b9b4;
    --ornament: #ead6c6;
  }
  * { margin: 0; padding: 0; box-sizing: border-box; }
  html, body { width: 846px; height: 1200px; overflow: hidden; background: var(--paper); }
  .card {
    position: relative;
    width: 846px;
    height: 1200px;
    background: var(--paper);
    overflow: hidden;
    font-family: "Marcellus", "Times New Roman", serif;
  }
  .card__sky {
    position: absolute;
    left: 0; top: 0;
    width: 846px; height: 685px;
    background: var(--cream);
  }
  .card__photo {
    position: absolute;
    left: 203px; top: 0;
    width: 643px; height: 602px;
    background: linear-gradient(160deg, var(--gerbera-red) 0%, var(--gerbera-deep) 100%);
  }
  .card__stem {
    position: absolute;
    top: 420px; bottom: 0;
    width: 2px;
    background: var(--stem-line);
  }
  .card__stem--left { left: 731px; }
  .card__stem--right { left: 743px; }
  .card__band {
    position: absolute;
    left: 0; top: 684px;
    width: 846px; height: 88px;
    background: var(--gerbera-red);
  }
  .card__title {
    position: absolute;
    left: 99px; top: 708px;
    font-size: 38px;
    line-height: 1;
    font-weight: 400;
    letter-spacing: 0.6px;
    color: var(--paper);
    white-space: nowrap;
  }
  .card__couple {
    position: absolute;
    left: 99px; top: 795px;
    font-size: 37px;
    line-height: 1;
    font-weight: 400;
    letter-spacing: 0.6px;
    color: var(--gerbera-red);
    white-space: nowrap;
  }
  .card__rule {
    position: absolute;
    left: 0; top: 1096px;
    width: 846px; height: 4px;
    background: var(--gerbera-red);
  }
  .card__blossom {
    position: absolute;
    border-radius: 50%;
    background: var(--ornament);
  }
  .card__blossom--small { left: 652px; top: 1085px; width: 30px; height: 30px; }
  .card__blossom--large { left: 712px; top: 1070px; width: 56px; height: 56px; }
</style>
</head>
<body>
  <main class="card">
    <div class="card__sky"></div>
    <div class="card__photo" role="img" aria-label="Foto einer roten Gerberablüte, angeschnitten oben rechts"></div>
    <div class="card__stem card__stem--left"></div>
    <div class="card__stem card__stem--right"></div>
    <div class="card__band"></div>
    <h1 class="card__title">EINLADUNG ZUR HOCHZEIT</h1>
    <p class="card__couple">LENA &amp; JONAS</p>
    <div class="card__rule"></div>
    <div class="card__blossom card__blossom--small" role="img" aria-label="Kleine helle Zierblüte"></div>
    <div class="card__blossom card__blossom--large" role="img" aria-label="Helle Zierblüte"></div>
  </main>
</body>
</html>
```